Stonebrook Business Card Redesign & Logo Update

We need to update our business cards to something more modern and fresh. Stonebrook can provide the current color schemes and old design examples, but welcome creativity in helping us with this redesign. PLEASE NOTE that we no longer utilize the "tree" and/or "leaf" imagery in our branding. If able would apprecaite an update on the quality of our "words only" logo in Ai. / PNG formats too.

Target Market(s)

Investors, landowners, corporate partners, contractors

Industry/Entity Type

Environmental Restoration & Conservation

Contact Information for Business Card

Logo, persons name, title, mailing address, phone and email, website url

Font styles to use
Other font styles liked:
• Merriweather

Requirements
Nice to have
• Logo, persons name, title, mailing address, phone and email, website url, but open to ideams
Should not have
• No all back backgrounds

```html
<!DOCTYPE html>
<html lang="en">
<head>
<meta charset="utf-8">
<title>Stonebrook Business Card</title>
<link rel="stylesheet" href="https://fonts.googleapis.com/css2?family=Bebas+Neue&family=Source+Sans+3:wght@400;700&display=swap">
<style>
  :root {
    --green: #12763d;
    --orange: #e67a22;
    --paper: #f4f4f4;
    --ink: #111111;
    --white: #ffffff;
    --backdrop: #e4e4e4;
  }
  html, body {
    margin: 0;
    width: 1200px;
    height: 960px;
    overflow: hidden;
    background: var(--backdrop);
  }
  .stage { display: block; width: 1200px; height: 960px; }
  .wordmark { font-family: "Bebas Neue", sans-serif; letter-spacing: 1px; }
  .tagline { font-family: "Bebas Neue", sans-serif; letter-spacing: 0.3px; }
  .person-name { font-family: "Source Sans 3", sans-serif; font-weight: 700; font-size: 19px; fill: var(--white); }
  .person-title { font-family: "Source Sans 3", sans-serif; font-weight: 400; font-size: 15px; fill: var(--white); }
  .contact-line { font-family: "Source Sans 3", sans-serif; font-weight: 400; font-size: 15.5px; fill: var(--white); }
  .contact-icon { fill: none; stroke: var(--orange); stroke-width: 1.4; stroke-linecap: round; stroke-linejoin: round; }
</style>
</head>
<body>
<svg class="stage" viewBox="0 0 1200 960" xmlns="http://www.w3.org/2000/svg">
  <defs>
    <clipPath id="front-card-shape"><rect x="296" y="105" width="612" height="350" rx="22"/></clipPath>
    <clipPath id="back-card-shape"><rect x="296" y="509" width="612" height="349" rx="22"/></clipPath>
  </defs>

  <!-- Front side -->
  <g class="card card-front" clip-path="url(#front-card-shape)">
    <rect x="296" y="105" width="612" height="350" fill="var(--green)"/>
    <rect class="accent-band" x="592" y="225" width="316" height="72" fill="var(--orange)"/>
    <text class="wordmark" x="417" y="295" font-size="82" fill="var(--white)">STONEBROOK</text>
    <text class="tagline" x="427" y="328" font-size="30" fill="var(--white)">ENVIRONMENTAL CREDIT COMPANY</text>
  </g>

  <!-- Back side -->
  <g class="card card-back" clip-path="url(#back-card-shape)">
    <rect x="296" y="509" width="612" height="349" fill="var(--paper)"/>
    <text class="wordmark" x="338" y="600" font-size="66" fill="var(--green)">STONEBROOK</text>
    <text class="tagline" x="347" y="628" font-size="25" fill="var(--ink)">ENVIRONMENTAL CREDIT COMPANY</text>

    <path class="contact-panel" d="M296 695 L578 695 L605 738 Q610 746 620 746 L648 746 L703 858 L296 858 Z" fill="var(--green)"/>
    <path class="name-banner" d="M573 663 L908 663 L908 741 L618 741 Q606 741 600 731 Z" fill="var(--orange)" stroke="var(--white)" stroke-width="4"/>

    <text class="person-name" x="878" y="698" text-anchor="end">Daniel Harper</text>
    <text class="person-title" x="878" y="719" text-anchor="end">Owner</text>

    <!-- pin -->
    <path class="contact-icon" d="M346 735 C342 730 340.5 727.5 340.5 725.5 A5.5 5.5 0 0 1 351.5 725.5 C351.5 727.5 350 730 346 735 Z"/>
    <circle class="contact-icon" cx="346" cy="725.5" r="1.8"/>
    <text class="contact-line" x="358" y="735">418 Meadow Lane, Suite 210</text>
    <text class="contact-line" x="358" y="755">Fairview, CA 95012</text>

    <!-- phone -->
    <path class="contact-icon" d="M341 775 Q341 773 343 773 L344.5 776 L343 777.5 Q345 781 348.5 783 L350 781.5 L353 783 Q353 785 351 785 Q342 784 341 775 Z"/>
    <text class="contact-line" x="358" y="785">555-014-2398</text>

    <!-- envelope -->
    <rect class="contact-icon" x="340.5" y="795.5" width="12" height="9" rx="1"/>
    <path class="contact-icon" d="M340.5 796.5 L346.5 801 L352.5 796.5"/>
    <text class="contact-line" x="358" y="806">daniel@stonebrook.com</text>

    <!-- globe -->
    <circle class="contact-icon" cx="346.5" cy="821" r="6"/>
    <ellipse class="contact-icon" cx="346.5" cy="821" rx="2.6" ry="6"/>
    <path class="contact-icon" d="M340.5 821 L352.5 821"/>
    <text class="contact-line" x="358" y="826">www.stonebrook.com</text>
  </g>
</svg>
</body>
</html>
```